Statement of Professional Excellence

Our school community has create a statement of Professional Excellence at our school (TBS = The Birchfield School at Dunmore) This will be shared internally and with candidates interviewing at our school. We'd like a branded graphic that lists in an interesting way our statements:

Professional Excellence at TBS

We honor the whole child while embracing them where they are.
We are mission-driven individuals whose dedication to our students motivates our daily work.
We bring flexible thinking to allow the needs of the students to drive the learning.
We are patient, nurturing, empathetic, and compassionate people.
We value, trust, and support each other.
We learn and we teach.
We lean into and celebrate diversity.
We build trust through genuine partnerships with families.
We are quirky, fun and proud of it.

```html
<!DOCTYPE html>
<html lang="en">
<head>
<meta charset="utf-8">
<title>Characteristics of Professional Excellence – The Birchfield School at Dunmore</title>
<link rel="stylesheet" href="https://fonts.googleapis.com/css2?family=Cormorant+Garamond:wght@700&family=Fira+Sans:ital,wght@1,700&display=swap">
<style>
  :root {
    --backdrop: #d3d4d6;
    --sheet: #eff0f2;
    --gold: #c8aa2e;
    --navy: #152c4e;
    --navy-deep: #0c1f3b;
    --ink-light: #e9ebef;
  }
  * { box-sizing: border-box; margin: 0; padding: 0; }
  html, body {
    width: 1180px;
    height: 1200px;
    overflow: hidden;
    background: var(--backdrop);
  }
  .sheet {
    position: absolute;
    left: 154px;
    top: 30px;
    width: 872px;
    height: 1140px;
    background: var(--sheet);
  }
  .title-band {
    position: absolute;
    left: 17px;
    top: 14px;
    width: 841px;
    height: 108px;
    background: var(--gold);
    display: flex;
    align-items: center;
    justify-content: center;
  }
  .title {
    font-family: "Cormorant Garamond", Georgia, serif;
    font-weight: 700;
    font-variant: small-caps;
    font-size: 54px;
    line-height: 47px;
    letter-spacing: 2px;
    color: var(--navy);
    text-align: center;
  }
  .school-name {
    position: absolute;
    left: 0;
    right: 0;
    top: 146px;
    text-align: center;
    font-family: "Cormorant Garamond", Georgia, serif;
    font-weight: 700;
    font-size: 32px;
    line-height: 36px;
    color: var(--navy);
  }
  .statements {
    position: absolute;
    left: 16px;
    top: 254px;
    width: 843px;
    display: grid;
    grid-template-columns: repeat(3, 269px);
    grid-template-rows: repeat(3, 277px);
    column-gap: 18px;
    row-gap: 19px;
    list-style: none;
  }
  .statement {
    background: linear-gradient(180deg, var(--navy) 0%, var(--navy-deep) 100%);
    display: flex;
    flex-direction: column;
    align-items: center;
    padding: 22px 14px 0;
  }
  .statement-mark {
    width: 84px;
    height: 84px;
    flex: none;
  }
  .statement-text {
    margin-top: 32px;
    font-family: "Fira Sans", Arial, sans-serif;
    font-style: italic;
    font-weight: 700;
    font-size: 20px;
    line-height: 26px;
    color: var(--ink-light);
    text-align: center;
  }
</style>
</head>
<body>
  <main class="sheet">
    <header class="title-band">
      <h1 class="title">Characteristics of<br>Professional Excellence</h1>
    </header>
    <p class="school-name">The Birchfield School<br>at Dunmore</p>
    <ul class="statements">
      <li class="statement">
        <svg class="statement-mark" viewBox="0 0 84 84" aria-hidden="true"><circle cx="42" cy="42" r="39" fill="none" stroke="#e9ebef" stroke-width="2.5"/><circle cx="42" cy="42" r="12" fill="#c8aa2e"/></svg>
        <p class="statement-text">We honor the whole child while embracing them where they are.</p>
      </li>
      <li class="statement">
        <svg class="statement-mark" viewBox="0 0 84 84" aria-hidden="true"><circle cx="42" cy="42" r="39" fill="none" stroke="#e9ebef" stroke-width="2.5"/><circle cx="42" cy="42" r="12" fill="#c8aa2e"/></svg>
        <p class="statement-text">We are mission-driven individuals whose dedication to our students motivates our daily work.</p>
      </li>
      <li class="statement">
        <svg class="statement-mark" viewBox="0 0 84 84" aria-hidden="true"><circle cx="42" cy="42" r="39" fill="none" stroke="#e9ebef" stroke-width="2.5"/><circle cx="42" cy="42" r="12" fill="#c8aa2e"/></svg>
        <p class="statement-text">We bring flexible thinking to allow the needs of the students to drive the learning.</p>
      </li>
      <li class="statement">
        <svg class="statement-mark" viewBox="0 0 84 84" aria-hidden="true"><circle cx="42" cy="42" r="39" fill="none" stroke="#e9ebef" stroke-width="2.5"/><circle cx="42" cy="42" r="12" fill="#c8aa2e"/></svg>
        <p class="statement-text">We value, trust, and support each other.</p>
      </li>
      <li class="statement">
        <svg class="statement-mark" viewBox="0 0 84 84" aria-hidden="true"><circle cx="42" cy="42" r="39" fill="none" stroke="#e9ebef" stroke-width="2.5"/><circle cx="42" cy="42" r="12" fill="#c8aa2e"/></svg>
        <p class="statement-text">We are patient, nurturing, empathetic, and compassionate people.</p>
      </li>
      <li class="statement">
        <svg class="statement-mark" viewBox="0 0 84 84" aria-hidden="true"><circle cx="42" cy="42" r="39" fill="none" stroke="#e9ebef" stroke-width="2.5"/><circle cx="42" cy="42" r="12" fill="#c8aa2e"/></svg>
        <p class="statement-text">We learn and we teach.</p>
      </li>
      <li class="statement">
        <svg class="statement-mark" viewBox="0 0 84 84" aria-hidden="true"><circle cx="42" cy="42" r="39" fill="none" stroke="#e9ebef" stroke-width="2.5"/><circle cx="42" cy="42" r="12" fill="#c8aa2e"/></svg>
        <p class="statement-text">We lean into and celebrate diversity.</p>
      </li>
      <li class="statement">
        <svg class="statement-mark" viewBox="0 0 84 84" aria-hidden="true"><circle cx="42" cy="42" r="39" fill="none" stroke="#e9ebef" stroke-width="2.5"/><circle cx="42" cy="42" r="12" fill="#c8aa2e"/></svg>
        <p class="statement-text">We build trust through genuine partnerships with families.</p>
      </li>
      <li class="statement">
        <svg class="statement-mark" viewBox="0 0 84 84" aria-hidden="true"><circle cx="42" cy="42" r="39" fill="none" stroke="#e9ebef" stroke-width="2.5"/><circle cx="42" cy="42" r="12" fill="#c8aa2e"/></svg>
        <p class="statement-text">We are quirky, fun and proud of it.</p>
      </li>
    </ul>
  </main>
</body>
</html>
```